Double Sided A4 Bi-Fold Brochure - very clear scope included

I have created a package which outlines the design requirements for an A4 brochure which folds twice to a DL size.

I would like whoever works on this project to look at the plant pictures taken in our reception area and use this for inspiration to style the brochure. So incorporate plants into the them/styling.

In the package you will find page layouts. Text outlines. Price schedules. Grouped pictures.

If you have any questions just ask

Thanks

Target Market(s)

Those seeking medical treatment for injury and chronic disease

Industry/Entity Type

Physical Therapy

Colors
acd036
9bcb3b

Requirements
Must have
• Must have a plant theme (not over powering).
• MUST use the green colours in our Logo.
Nice to have
• Use the pictures that we have included in the package where possible

```html
<!DOCTYPE html>
<html lang="en">
<head>
<meta charset="utf-8">
<title>Fernleaf Physio – Pilates Brochure</title>
<link href="https://fonts.googleapis.com/css2?family=Source+Sans+3:wght@400;600;700&display=swap" rel="stylesheet">
<style>
:root{
  --leaf:#9bcb3b;
  --lime:#acd036;
  --ink:#1e1e1e;
  --paper:#ffffff;
  --mist:#eef5df;
  --wave:#e4f0cc;
}
*{margin:0;padding:0;box-sizing:border-box}
html,body{width:1200px;height:849px;overflow:hidden;background:var(--paper)}
body{font-family:"Source Sans 3",Arial,sans-serif;color:var(--ink);position:relative}
.brochure{position:relative;width:1200px;height:849px;overflow:hidden}
.panel{position:absolute;top:0;height:849px}
.panel--intro{left:0;width:406px}
.panel--schedule{left:406px;width:395px}
.panel--pricing{left:801px;width:399px}
.waves{position:absolute;left:0;top:0}
.heading{color:var(--leaf);font-weight:700;letter-spacing:3px;font-size:20px;text-align:center;position:absolute}
.intro-copy{position:absolute;left:41px;width:340px;font-size:14px;line-height:18.5px;text-align:justify}
.intro-copy p+p{margin-top:18px}
.subheading{position:absolute;left:35px;top:410px;color:var(--leaf);font-weight:700;font-size:16px;letter-spacing:.5px}
.suit-list{position:absolute;left:35px;top:451px;list-style:none;font-size:14px;line-height:18.5px}
.suit-list li{position:relative;padding-left:20px}
.suit-list li::before{content:"";position:absolute;left:0;top:5px;width:9px;height:9px;border-radius:50%;background:var(--leaf)}
.claim-note{position:absolute;left:35px;top:650px;width:346px;font-size:14px;line-height:18.5px;text-align:justify}
.tab{position:absolute;background:var(--leaf);color:#fff;font-weight:700;letter-spacing:3px;font-size:15px;padding-left:22px;display:flex;align-items:center}
.timetable{position:absolute;left:24px;top:328px;border-collapse:collapse;font-size:15px}
.timetable td{height:37px;vertical-align:middle}
.timetable .day{color:var(--leaf);font-weight:700;width:151px;letter-spacing:.3px}
.timetable .times{font-weight:600}
.price-group{position:absolute;left:11px;width:380px;font-size:13.5px;line-height:18.5px}
.price-group h3{color:var(--leaf);font-size:17px;font-weight:700;line-height:21px}
.price-group h3 small{color:var(--ink);font-size:13.5px;font-weight:400}
.price-row{display:flex}
.price-row span:first-child{width:240px}
.map-area{position:absolute;left:85px;top:530px;width:172px;height:172px}
.contact{position:absolute;left:0;width:399px;text-align:center;color:var(--leaf);font-weight:700}
</style>
</head>
<body>
<div class="brochure">

  <section class="panel panel--intro">
    <svg class="waves" width="406" height="849" aria-hidden="true">
      <path d="M0 330 C110 300 250 250 406 270 L406 300 C260 285 120 330 0 360Z" fill="var(--wave)"/>
      <path d="M0 380 C140 350 280 320 406 350 L406 372 C280 345 130 380 0 410Z" fill="var(--mist)"/>
    </svg>
    <h1 class="heading" style="left:0;top:34px;width:406px">PILATES</h1>
    <div class="intro-copy" style="top:96px">
      <p>All of our individual and group pilates sessions are conducted by highly experienced physiotherapists. All of whom have a minimum of 20 years experience.</p>
      <p>Clients can progress from individual treatment and management of acute pain, through to strengthening and return to usual activities.</p>
      <p>Our therapists are always on hand to make adjustments to your exercises and cater for your individual needs, with a professional understanding of your problem.</p>
    </div>
    <h2 class="subheading">PILATES IS SUITABLE FOR:</h2>
    <ul class="suit-list">
      <li>Core weakness &amp; starting an exercise programme</li>
      <li>Recovering from injury</li>
      <li>Managing back or neck pain</li>
      <li>Advanced core strengthening</li>
      <li>Pregnancy and after delivery</li>
      <li>Part of a chronic disease management plan (EPC)</li>
      <li>Posture</li>
      <li>Flexibility</li>
      <li>General exercise</li>
    </ul>
    <p class="claim-note">Pilates is claimable on your private health insurance extras under your Physiotherapy benefits and we can process your ClaimPoint claim on the spot.</p>
  </section>

  <section class="panel panel--schedule">
    <svg class="waves" width="395" height="849">
      <defs>
        <linearGradient id="studio" x1="0" y1="0" x2="1" y2="1">
          <stop offset="0" stop-color="#d9dcdc"/><stop offset="1" stop-color="#8e9496"/>
        </linearGradient>
        <linearGradient id="treatment" x1="0" y1="0" x2="1" y2="1">
          <stop offset="0" stop-color="#e8eaea"/><stop offset="1" stop-color="#6f6a66"/>
        </linearGradient>
      </defs>
      <rect width="395" height="300" fill="url(#studio)" role="img" aria-label="Photo of a group pilates class on reformer machines"/>
      <rect y="520" width="395" height="329" fill="url(#treatment)" role="img" aria-label="Photo of a therapist giving a shoulder massage"/>
      <path d="M0 258 C120 250 260 270 395 240 L395 580 C260 540 130 535 0 560Z" fill="var(--paper)"/>
      <path d="M0 546 C130 515 270 520 395 560 L395 580 C260 545 130 540 0 565Z" fill="var(--wave)"/>
    </svg>
    <div class="tab" style="left:0;top:34px;width:206px;height:26px">PILATES CLASS</div>
    <h2 class="heading" style="left:0;top:284px;width:395px;font-size:19px">PILATES TIMETABLE</h2>
    <table class="timetable">
      <tr><td class="day">MONDAY</td><td class="times">9:15, 10:15, 5:30</td></tr>
      <tr><td class="day">TUESDAY</td><td class="times">7:45, 9:15, 10:15, 3:30, 5:30</td></tr>
      <tr><td class="day">WEDNESDAY</td><td class="times">9:15, 10:15, 11:15, 5:30</td></tr>
      <tr><td class="day">THURSDAY</td><td class="times">7:45, 9:15, 10:15, 11:15</td></tr>
      <tr><td class="day">FRIDAY</td><td class="times">9:15, 10:15</td></tr>
      <tr><td class="day">SATURDAY</td><td class="times">8:45, 9:30</td></tr>
    </table>
    <div class="tab" style="left:0;top:593px;width:136px;height:24px">MASSAGE</div>
  </section>

  <section class="panel panel--pricing">
    <svg class="waves" width="399" height="849" aria-hidden="true">
      <path d="M0 330 C120 300 260 390 399 350 L399 372 C260 410 120 325 0 352Z" fill="var(--wave)"/>
    </svg>
    <h2 class="heading" style="left:0;top:28px;width:399px">PRICING</h2>
    <div class="price-group" style="top:70px">
      <h3>PHYSIO <small>(covered by health insurance)</small></h3>
      <div class="price-row"><span>Initial</span><span>$85 - 45 mins</span></div>
      <div class="price-row"><span>Standard</span><span>$75 - 30 mins</span></div>
      <div class="price-row"><span>Initial Concession</span><span>$75</span></div>
      <div class="price-row"><span>Standard Concession</span><span>$60</span></div>
      <div class="price-row"><span>Home Visit</span><span>$110</span></div>
    </div>
    <div class="price-group" style="top:200px">
      <h3>PILATES <small>(covered by health insurance)</small></h3>
      <div class="price-row"><span>Individually</span><span>$30</span></div>
      <div class="price-row"><span>Each as a group of 5($25 X 5)</span><span>$125</span></div>
      <div class="price-row"><span>1v1 Pilates</span><span>$65</span></div>
      <div class="price-row"><span>Pilates Assessment</span><span>$80</span></div>
      <div class="price-row"><span>Kids (14 or Younger) Standard</span><span>$75</span></div>
      <div class="price-row"><span>Kids (14 or Younger) Cons.</span><span>$60</span></div>
    </div>
    <div class="price-group" style="top:347px">
      <h3>MASSAGE <small>(covered by health insurance)</small></h3>
      <div class="price-row"><span>1 Hour Massage</span><span>$85</span></div>
      <div class="price-row"><span>30 Minutes</span><span>$60</span></div>
    </div>
    <div class="price-group" style="top:420px">
      <h3>DRY NEEDLING WITH ACUPUNCTURE<br>NEEDLES <small>(covered by health insurance)</small></h3>
      <div class="price-row"><span></span><span>$90</span></div>
    </div>
    <div class="map-area" role="img" aria-label="Street map showing the clinic location" style="background:linear-gradient(135deg,#f3f8e8,#dcecb8)"></div>
    <p class="contact" style="top:742px;font-size:15px">4/118 Elm Terrace Kenwood</p>
    <p class="contact" style="top:762px;font-size:15px">Ph : 70140388 &nbsp;&nbsp;&nbsp;&nbsp;&nbsp;&nbsp; Fax 83920517</p>
    <p class="contact" style="top:795px;font-size:18px">fernleafphysio.com.au</p>
  </section>

</div>
</body>
</html>
```